Post Lockdown Ortho Special

We are running a special for (Ortho) Braces/Clear Aligner (Quorventa), till July 31st 2020. Up to $2,000 off with free Consultation and Xrays.

We need a ad to run in different formats.

Maybe something with: what better time to get braces when you have to wear a mask all the time.

Trying to rebuild our business and get people in for free consultations.

```html
<!DOCTYPE html>
<html lang="en">
<head>
<meta charset="utf-8">
<title>Harborline Family Dentistry – Ortho Special</title>
<link rel="stylesheet" href="https://fonts.googleapis.com/css2?family=Poppins:wght@300;600;700&display=swap">
<style>
  :root {
    --purple: #5f4b97;
    --purple-box: #654f95;
    --grey-box: #9aa1ab;
    --ink: #3a3a3a;
    --muted: #8a8a93;
    --white: #ffffff;
    --frame: #cfcfd4;
    --photo-warm: #d8c6b4;
    --photo-blue: #9bb0d6;
    --photo-cream: #ece6da;
  }
  * { margin: 0; padding: 0; box-sizing: border-box; }
  html, body { width: 849px; height: 1200px; overflow: hidden; background: var(--white); }
  .ad {
    position: relative; width: 849px; height: 1200px; overflow: hidden;
    background: var(--white); border: 1px solid var(--frame);
    font-family: "Poppins", sans-serif;
  }
  .headline {
    position: absolute; left: 53px; top: 48px; width: 745px;
    color: var(--purple); font-weight: 700; font-size: 37px; line-height: 45px;
    letter-spacing: -0.2px;
  }
  .headline span { display: block; }
  .headline .second { text-align: right; }
  .hero-photo {
    position: absolute; left: 0; top: 160px; width: 849px; height: 565px;
    background: linear-gradient(105deg, var(--photo-warm) 0%, var(--photo-blue) 50%, var(--photo-cream) 100%);
  }
  .intro {
    position: absolute; left: 34px; top: 751px; width: 404px;
    color: var(--ink); font-weight: 300; font-size: 14.6px; line-height: 31.2px;
  }
  .intro span { display: block; text-align: justify; text-align-last: justify; white-space: nowrap; }
  .intro span.last { text-align-last: left; }
  .offer-box {
    position: absolute; left: 490px; top: 756px; width: 359px; height: 230px;
    background: var(--purple-box); color: var(--white);
    padding: 14px 10px 0 33px;
    font-weight: 700; font-size: 26.5px; line-height: 38.8px;
  }
  .discount-box {
    position: absolute; left: 0; top: 1034px; width: 434px; height: 120px;
    background: var(--grey-box); color: var(--white);
    padding: 22px 0 0 34px;
    font-weight: 700; font-size: 25.5px; line-height: 36px;
  }
  .practice {
    position: absolute; left: 466px; top: 1046px; width: 370px; height: 96px;
    display: flex; align-items: center; gap: 18px;
  }
  .practice-mark { width: 56px; height: 56px; border-radius: 50%; background: #c9bde0; flex: none; }
  .practice-name {
    color: var(--purple); font-weight: 600; font-size: 20px; line-height: 24px;
  }
  .practice-doctor {
    margin-top: 6px; padding-top: 5px; border-top: 1px solid var(--muted);
    color: var(--muted); font-weight: 300; font-size: 12px; letter-spacing: 1.5px;
    text-transform: uppercase;
  }
</style>
</head>
<body>
  <main class="ad">
    <h1 class="headline">
      <span class="first">Your dental health and</span>
      <span class="second">well being are our top priority.</span>
    </h1>

    <div class="hero-photo" role="img" aria-label="Photo of a smiling young boy in a blue dental chair giving a thumbs up while a masked dentist examines his teeth"></div>

    <p class="intro">
      <span>Everyday, the Harborline teams put patient and</span>
      <span>employee well-being first, providing clean, safe</span>
      <span>treatment environments for all. We know COVID-19,</span>
      <span>commonly called coronavirus, is a concern for</span>
      <span>everyone. Our commitment is to say "Yes" to patient</span>
      <span>care. We want to deliver the same quality care in</span>
      <span>these circumstance while helping prevent the</span>
      <span class="last">spread of COVID-19.</span>
    </p>

    <div class="offer-box">We are running a<br>special for (Ortho)<br>Braces/Clear Aligner<br>(Quorventa), till<br>July 31st 2020.</div>

    <div class="discount-box">Up to $2,000 off with<br>free Consultation and Xrays.</div>

    <div class="practice">
      <div class="practice-mark"></div>
      <div>
        <div class="practice-name">Harborline Family Dentistry</div>
        <div class="practice-doctor">Dr Miriam Ashdown</div>
      </div>
    </div>
  </main>
</body>
</html>
```